Poster for Indie Film: a Love Story set in The Hamptons

Need striking key marketing art for an indie film called CORVELL CAUSEWAY. It's a teen love story against the tensions between the locals and the summer crowd in the Hamptons.

It's about a local boy falling in love with a rich girl from New York City. There's also a sub-plot about the local being welcomed into the elite social class on the other side of town, but ONLY if he covers up a rich family's hit-and-run scandal.

It's co-written and directed by East Hampton locals. Here's my FlickRolls page: www.flickrolls.example/name/zz7730162/ and my script portfolio page www.TarrenVolke.example

The thing is, if/when this film gets made, a distributor will likely make the poster by slapping on the three stars of the film: the rich girl, the blue collar boy, and the girl's dad (an Dorian Fesk type who drives the sub-plot). But since we don't have actors yet, we've gotta get creative.

We can do it!

I've uploaded a detailed description of what we need, along with comments about other comparable posters. You can even read the script. The first 2 pages will give you the scoop on the sub-plot.

In general, think: iconic, striking and urgent.

Target Market(s)

The same people who saw PALE ORCHARD and THE SECRETS OF STANDING BY THE WINDOW.

Industry/Entity Type

Marketing

Requirements
Must have
• SPECS:
- The final image will be used digitally on PDFs and may be printed at 8.5 X 11inches. So 300 DPI is preferred. But it would also be very helpful to be able to print at the standard full size 24" x 36 inches. So if possible, a final version in that size as well, maybe at 150 DPI,if 300dpi for 24x36 is too huge of a file.
Nice to have
• - Silhouettes and/or obscured faces may work nicely for the characters.

- It's possible we could find one simple image of an object that conveys "opulence" to suggest the themes of the story.

- You can try this tagline: "His World. Her World. Collide in The Hamptons." Which is kinda melodramatic, but MIGHT work if the image was rough and raw to contrast that fluffiness. Or I'm open to a riff on that tagline. Or maybe no tagline at all.

- If you want to throw in a credit block, here it is:

MARIGOLD PICTURES presents a film by TARREN VOLKE
CORVELL CAUSEWAY
music by SIMON KETTERIDGE
written by TARREN VOLKE and PAUL RADEMACHER
co-produced by NED FARLOW PAUL RADEMACHER TARREN VOLKE
produced by COLIN ABERNATHY
directed by TARREN VOLKE
Should not have
• Obviously, can't have recognizable actors, or any actor images you don't have the rights to.

```html
<!DOCTYPE html>
<html lang="en">
<head>
<meta charset="utf-8">
<title>Corvell Causeway — Poster</title>
<link rel="stylesheet" href="https://fonts.googleapis.com/css2?family=Archivo+Black&family=Arimo:wght@400&display=swap">
<style>
  :root {
    --paper: #ffffff;
    --ink: #111111;
    --surf-cyan: #8fd3d9;
    --sunset-pink: #ef8cba;
    --mask-teal: #5f9ea0;
    --mask-light: #c9e9ec;
  }
  html, body {
    margin: 0;
    padding: 0;
    overflow: hidden;
    background: var(--paper);
  }
  .poster {
    position: relative;
    width: 933px;
    height: 1200px;
    background: var(--paper);
    overflow: hidden;
    font-family: "Arimo", Arial, sans-serif;
    color: var(--ink);
  }
  .key-art {
    position: absolute;
    left: 366px;
    top: 132px;
    width: 214px;
    height: 244px;
  }
  .title-art {
    position: absolute;
    left: 0;
    top: 420px;
    width: 933px;
    height: 290px;
  }
  .title-word {
    font-family: "Archivo Black", "Arial Black", sans-serif;
    font-size: 158px;
  }
  .title-word.cyan { fill: var(--surf-cyan); }
  .title-word.pink { fill: var(--sunset-pink); }
  .tagline {
    position: absolute;
    top: 780px;
    left: 0;
    width: 933px;
    margin: 0;
    text-align: center;
    font-size: 25px;
    line-height: 1.2;
  }
  .credits {
    position: absolute;
    top: 986px;
    left: 0;
    width: 933px;
    margin: 0;
    text-align: center;
    font-size: 14px;
    line-height: 1;
  }
  .credits p { margin: 0 0 11.5px; }
  .credits p.tight { margin-bottom: 4px; }
</style>
</head>
<body>
<main class="poster">

  <svg class="key-art" viewBox="0 0 214 244" role="img" aria-label="Illustration of a snorkel mask with its breathing tube">
    <defs>
      <linearGradient id="maskTone" x1="0" y1="0" x2="0" y2="1">
        <stop offset="0" stop-color="var(--mask-light)"/>
        <stop offset="1" stop-color="var(--mask-teal)"/>
      </linearGradient>
    </defs>
    <rect x="0" y="0" width="214" height="244" fill="url(#maskTone)"/>
  </svg>

  <svg class="title-art" viewBox="0 0 933 290" aria-label="CORVELL CAUSEWAY">
    <text class="title-word cyan" x="158" y="129" textLength="625" lengthAdjust="spacingAndGlyphs">CORVELL</text>
    <text class="title-word pink" x="158" y="275" textLength="625" lengthAdjust="spacingAndGlyphs">CAUSEWAY</text>
  </svg>

  <p class="tagline">“His World. Her World. Collide in The Hamptons”</p>

  <section class="credits">
    <p>MARIGOLD PICTURES presents a film by</p>
    <p>TARREN VOLKE</p>
    <p>CORVELL CAUSEWAY</p>
    <p>music by SIMON KETTERIDGE</p>
    <p>written by TARREN VOLKE and PAUL RADEMACHER</p>
    <p class="tight">co-produced by NED FARLOW PAUL RADEMACHER TARREN VOLKE</p>
    <p class="tight">produced by COLIN ABERNATHY</p>
    <p>directed by TARREN VOLKE</p>
  </section>

</main>
</body>
</html>
```